Wordpress website for Dance Studio

Hi there, I am looking for Wordpress Website for dance studio. Happy for designed to use available themes. Would like a few pages setup and I can do the rest.

Other things I would like included in this theme :

Nice images page OR moving banner
Blog
Ability for youtubes

Other than that, simple requirements, just a gorgeous looking landing page/site etc.

Target Market(s)

Dance mums and kids (dancers)

Industry/Entity Type

Dance and Performancer

Coding

Coded - Design and coding required

Number of Pages Required

4 page

Font styles to use
Sans Serif

Colors
EB3D1F
EC4F4E
F09395
F8D3D4
FCEDEE

Requirements
Must have
• Wordpress theme
Nice to have
• Artistic, graphical, dance studio theme

```html
<!DOCTYPE html>
<html lang="en">
<head>
<meta charset="utf-8">
<title>Dance Studio</title>
<link href="https://fonts.googleapis.com/css2?family=Josefin+Sans:wght@300;400;600;700&display=swap" rel="stylesheet">
<style>
:root{
  --red:#EC4F4E;
  --red-deep:#EB3D1F;
  --pink:#F09395;
  --blush:#F8D3D4;
  --mist:#FCEDEE;
  --ink:#222;
  --muted:#666;
  --white:#fff;
}
*{margin:0;padding:0;box-sizing:border-box}
html,body{width:1200px;height:3447px;overflow:hidden}
body{position:relative;font-family:'Josefin Sans',sans-serif;color:var(--ink);background:var(--white)}
.abs{position:absolute}
.btn{position:absolute;display:flex;align-items:center;justify-content:center;background:var(--red);color:var(--white);border-radius:30px;font-weight:700;letter-spacing:3px;font-size:18px}

/* hero */
.hero-photo{left:0;top:0;width:1200px;height:730px;
  background:
    radial-gradient(ellipse 170px 260px at 600px 330px,rgba(240,190,192,.75),rgba(240,190,192,0) 100%),
    radial-gradient(ellipse 210px 300px at 930px 290px,rgba(244,200,202,.8),rgba(244,200,202,0) 100%),
    radial-gradient(ellipse 150px 240px at 760px 320px,rgba(240,196,198,.7),rgba(240,196,198,0) 100%),
    linear-gradient(180deg,#8f8f98 0%,#a3a2aa 40%,#8a8990 62%,#6b6a70 80%,#4f4e53 100%)}
.hero-wave{left:0;top:540px}
.brand{left:74px;top:42px;display:flex;align-items:center;gap:14px;color:var(--white);font-size:24px;font-weight:400}
.brand-mark{width:62px;height:62px;border-radius:50%;background:var(--red)}
.nav{top:24px;left:791px}
.nav a{color:var(--white);text-decoration:none;font-size:16px;position:absolute;white-space:nowrap}
.nav .active::after{content:"";position:absolute;left:50%;top:24px;width:7px;height:7px;margin-left:-3px;border-radius:50%;background:var(--red)}
.hero-kicker{left:71px;top:218px;font-size:44px;font-weight:300;color:var(--white)}
.hero-title{left:71px;top:266px;font-size:76px;font-weight:700;color:var(--white);line-height:1}
.slides{left:1060px;top:244px;width:70px}
.slides div{position:absolute;right:0;font-size:14px;font-weight:600;color:var(--white);white-space:nowrap}
.slides .on{color:var(--red)}
.slides span{display:inline-block;width:44px;height:1px;background:rgba(255,255,255,.6);vertical-align:middle;margin-right:6px}
.slides .on span{background:var(--red)}

/* about */
.about-art{left:0;top:755px}
.welcome{left:612px;top:855px;font-size:33px;font-weight:300}
.about-title{left:612px;top:892px;font-size:60px;font-weight:600}
.about-copy{left:612px;top:972px;width:500px;font-size:20px;line-height:27px;font-weight:300;color:#444}

/* video */
.video-photo{left:0;top:1298px;width:1200px;height:525px;
  background:
    radial-gradient(ellipse 140px 110px at 330px 330px,rgba(250,232,234,.95),rgba(250,232,234,0) 100%),
    radial-gradient(ellipse 120px 100px at 480px 340px,rgba(250,234,236,.9),rgba(250,234,236,0) 100%),
    radial-gradient(ellipse 110px 90px at 600px 320px,rgba(250,234,236,.85),rgba(250,234,236,0) 100%),
    radial-gradient(ellipse 100px 240px at 960px 260px,rgba(60,58,60,.35),rgba(60,58,60,0) 100%),
    linear-gradient(180deg,#dcd8d5 0%,#cdc8c5 60%,#bfb9b6 100%)}
.play{left:561px;top:1500px}
.video-label{left:0;width:1200px;top:1594px;text-align:center;color:var(--white);font-size:30px;font-weight:600;letter-spacing:1px}

/* blog */
.blog-title{left:69px;top:1905px;font-size:62px;font-weight:600}
.card{position:absolute;top:2003px;width:336px;height:451px;background:var(--white);border-radius:8px;box-shadow:0 2px 10px rgba(0,0,0,.14);overflow:hidden}
.card-photo{height:231px;background:radial-gradient(ellipse 90px 70px at 230px 150px,rgba(248,226,228,1),rgba(248,226,228,0) 100%),linear-gradient(180deg,#f1efee 0%,#e4dfdc 65%,#c9bcb3 100%)}
.card-photo.alt{background:radial-gradient(ellipse 120px 90px at 120px 130px,rgba(246,214,216,1),rgba(246,214,216,0) 100%),radial-gradient(ellipse 70px 110px at 290px 130px,rgba(90,80,80,.3),rgba(90,80,80,0) 100%),linear-gradient(160deg,#e8dedd,#d6c9c7)}
.card-photo.top{background:radial-gradient(circle 100px at 168px 115px,rgba(250,236,236,1),rgba(250,236,236,0) 100%),radial-gradient(ellipse 60px 40px at 170px 60px,rgba(120,95,85,.35),rgba(120,95,85,0) 100%),linear-gradient(160deg,#f2efed,#ddd5d2)}
.card-head{position:absolute;top:250px;left:0;right:0;height:52px}
.card-date{position:absolute;left:10px;top:0;color:var(--red);font-size:18px;line-height:22px}
.card-date b{display:block;font-size:25px;font-weight:400}
.card-date::after{content:"";position:absolute;left:44px;top:0;width:1px;height:50px;background:#999}
.card-heading{position:absolute;left:72px;top:2px;font-size:18px;font-weight:600;line-height:24px}
.card-text{position:absolute;top:320px;left:15px;width:305px;font-size:18px;line-height:25px;font-weight:300;color:#555}
.card-link{position:absolute;top:413px;left:14px;font-size:13px;font-weight:700;color:var(--red);letter-spacing:.5px}

/* contact */
.contact-bg{left:0;top:2500px}
.contact-art{left:0;top:2555px}
.touch-title{left:612px;top:2665px;font-size:39px;font-weight:300;color:var(--white)}
.field{position:absolute;background:var(--white);border-radius:4px;font-size:14px;color:#777;padding:17px 12px}
.send{left:1004px;top:2958px;width:124px;height:40px;border:2px solid var(--white);border-radius:20px;color:var(--white);font-size:12px;font-weight:600;display:flex;align-items:center;justify-content:center;position:absolute}
.rule{left:71px;top:3050px;width:1057px;height:1px;background:rgba(255,255,255,.4)}
.foot-h{top:3117px;font-size:19px;color:var(--white);position:absolute}
.foot-list{position:absolute;top:3163px;color:var(--white);font-size:14px;line-height:30px;list-style:none}
.foot-list li{display:flex;align-items:center;gap:8px}
.foot-about{position:absolute;left:594px;top:3165px;width:225px;color:var(--white);font-size:13.5px;line-height:24px}
.socials{left:71px;top:3265px;display:flex;gap:20px}
.socials i{width:13px;height:13px;border-radius:3px;border:1.6px solid var(--white);display:block}
.news-input{left:869px;top:3160px;width:258px;height:40px;border-radius:20px;background:var(--white);font-size:13px;color:#777;padding:13px 18px;position:absolute}
.news-btn{left:869px;top:3210px;width:258px;height:40px;border-radius:20px;background:var(--pink);color:var(--white);font-size:12px;font-weight:600;display:flex;align-items:center;justify-content:center;position:absolute}
.copyright{left:0;width:1200px;top:3411px;text-align:center;font-size:13px;color:#444}
.copyright em{font-style:normal;color:var(--red)}
</style>
</head>
<body>

<!-- Hero -->
<div class="abs hero-photo" role="img" aria-label="Young ballet students in pink leotards practising at the barre"></div>
<svg class="abs hero-wave" width="1200" height="200" viewBox="0 0 1200 200">
  <path d="M0 25 C120 0 220 30 330 80 C470 150 560 200 700 190 C850 180 950 105 1200 140 L1200 200 L0 200 Z" fill="#fff"/>
</svg>
<div class="abs brand"><span class="brand-mark"></span>Dance Studio</div>
<nav class="abs nav">
  <a class="active" style="left:0">Home</a>
  <a style="left:96px">About</a>
  <a style="left:193px">Blog</a>
  <a style="left:278px">Contact</a>
</nav>
<div class="abs hero-kicker">We Are Here For</div>
<div class="abs hero-title">Dance Studio</div>
<div class="btn" style="left:71px;top:375px;width:218px;height:58px">READ MORE</div>
<div class="abs slides">
  <div class="on" style="top:0"><span></span>01</div>
  <div style="top:66px"><span></span>02</div>
  <div style="top:132px">03</div>
</div>

<!-- About -->
<svg class="abs about-art" width="600" height="470" viewBox="0 0 600 470" role="img" aria-label="Dance teacher guiding a young ballerina in a split">
  <defs>
    <radialGradient id="aboutTone" cx="0.45" cy="0.5" r="0.6">
      <stop offset="0" stop-color="#f3d2d4"/>
      <stop offset="0.45" stop-color="#c9bfbf"/>
      <stop offset="1" stop-color="#8f8d8f"/>
    </radialGradient>
  </defs>
  <path d="M110 120 C130 40 230 10 300 40 C360 65 400 110 470 150 C560 205 570 290 530 340 C480 410 380 460 260 460 C150 460 80 420 75 350 C70 270 90 190 110 120 Z" fill="url(#aboutTone)"/>
  <path d="M255 30 C350 60 440 140 530 220 C580 270 560 360 480 400 C390 445 250 445 120 420 C40 400 45 320 80 250 C110 190 160 80 255 30" fill="none" stroke="#EC4F4E" stroke-width="2.5"/>
</svg>
<div class="abs welcome">Welcome to</div>
<div class="abs about-title">Dance Studio</div>
<p class="abs about-copy">Lorem ipsum dolor sit amet, consectetur adipiscing elit, sed do eiusmod tempor incididunt ut labore et dolore magna aliqua. Quis ipsum suspendisse ultrices gravida. Risus commodo viverra maecenas facilisis.</p>
<div class="btn" style="left:612px;top:1110px;width:218px;height:58px">READ MORE</div>

<!-- Video -->
<div class="abs video-photo" role="img" aria-label="Teacher and little ballerinas in tutus stretching in a bright studio"></div>
<svg class="abs play" width="78" height="78" viewBox="0 0 78 78">
  <circle cx="39" cy="39" r="37" fill="none" stroke="#EC4F4E" stroke-width="3"/>
  <path d="M30 24 L56 39 L30 54 Z" fill="none" stroke="#EC4F4E" stroke-width="3" stroke-linejoin="round"/>
</svg>
<div class="abs video-label">VIDEO</div>

<!-- Blog -->
<h2 class="abs blog-title">Latest Blog</h2>
<div class="btn" style="left:925px;top:1917px;width:203px;height:57px">VIEW ALL</div>

<article class="card" style="left:73px">
  <div class="card-photo" role="img" aria-label="Little ballerina in a tutu in a bright studio"></div>
  <div class="card-head"><div class="card-date">Jun<b>02</b></div><div class="card-heading">Lorem ipsum dolor sit amet, consectetur adipiscing</div></div>
  <p class="card-text">Lorem ipsum dolor sit amectetur adipiscing elit. In pretium ante quis nunc tincint maximus</p>
  <div class="card-link">READ MORE →</div>
</article>
<article class="card" style="left:433px">
  <div class="card-photo alt" role="img" aria-label="Teacher helping young ballerinas with a pose"></div>
  <div class="card-head"><div class="card-date">Jun<b>06</b></div><div class="card-heading">Lorem ipsum dolor sit amet, consectetur adipiscing</div></div>
  <p class="card-text">Lorem ipsum dolor sit amectetur adipiscing elit. In pretium ante quis nunc tincint maximus</p>
  <div class="card-link">READ MORE →</div>
</article>
<article class="card" style="left:792px">
  <div class="card-photo top" role="img" aria-label="Ballerinas seen from above joining hands in a circle"></div>
  <div class="card-head"><div class="card-date">Aug<b>18</b></div><div class="card-heading">Lorem ipsum dolor sit amet, consectetur adipiscing</div></div>
  <p class="card-text">Lorem ipsum dolor sit amectetur adipiscing elit. In pretium ante quis nunc tincint maximus</p>
  <div class="card-link">READ MORE →</div>
</article>

<!-- Contact & footer -->
<svg class="abs contact-bg" width="1200" height="947" viewBox="0 0 1200 947">
  <path d="M0 95 C150 140 300 120 450 80 C620 35 780 55 960 70 C1060 78 1130 55 1200 40 L1200 830 C1050 820 950 760 800 810 C650 860 560 900 420 895 C280 890 150 830 0 850 Z" fill="#EC4F4E"/>
  <path d="M975 25 C1000 0 1040 5 1080 30 C1110 50 1110 70 1080 90 C1040 120 1010 140 990 120 C960 90 950 50 975 25 Z" fill="#F09395"/>
</svg>
<svg class="abs contact-art" width="600" height="480" viewBox="0 0 600 480" role="img" aria-label="Dance teacher correcting young ballerinas at the barre">
  <defs>
    <radialGradient id="contactTone" cx="0.5" cy="0.45" r="0.6">
      <stop offset="0" stop-color="#f6e6e6"/>
      <stop offset="0.5" stop-color="#d3c8c4"/>
      <stop offset="1" stop-color="#a79b95"/>
    </radialGradient>
  </defs>
  <path d="M100 60 C180 10 330 20 450 30 C560 40 520 150 470 230 C420 310 390 390 320 440 C250 480 190 470 150 400 C110 330 60 250 40 160 C30 110 60 80 100 60 Z" fill="url(#contactTone)"/>
  <path d="M530 200 C560 290 480 370 380 400" fill="none" stroke="#fff" stroke-width="3"/>
</svg>
<div class="abs touch-title">Get In Touch Today</div>
<div class="field" style="left:612px;top:2727px;width:253px;height:49px">Name</div>
<div class="field" style="left:873px;top:2727px;width:255px;height:49px">Email</div>
<div class="field" style="left:612px;top:2785px;width:253px;height:50px">Phone</div>
<div class="field" style="left:873px;top:2785px;width:255px;height:50px">Subject</div>
<div class="field" style="left:612px;top:2843px;width:516px;height:105px">Your Message</div>
<div class="send">START NOW</div>

<div class="abs rule"></div>
<div class="foot-h" style="left:71px">Contact Us</div>
<ul class="foot-list" style="left:71px">
  <li><svg width="12" height="14" viewBox="0 0 12 14"><path d="M6 0a5 5 0 0 1 5 5c0 4-5 9-5 9S1 9 1 5a5 5 0 0 1 5-5z" fill="#fff"/><circle cx="6" cy="5" r="2" fill="#EC4F4E"/></svg>12 Arbour Lane, Sydney, Australia</li>
  <li><svg width="12" height="12" viewBox="0 0 12 12"><path d="M2 0l3 3-1.5 1.8a8 8 0 0 0 3.7 3.7L9 7l3 3-2 2C5 12 0 7 0 2z" fill="#fff"/></svg>+01 555 014 220</li>
  <li><svg width="12" height="12" viewBox="0 0 12 12"><circle cx="6" cy="6" r="6" fill="#fff"/><path d="M6 3v3.5l2 1.2" stroke="#EC4F4E" stroke-width="1.4" fill="none"/></svg>Monday - Friday: 8 AM - 5 PM</li>
</ul>
<div class="abs socials" aria-label="Social links"><i></i><i></i><i></i><i></i></div>

<div class="foot-h" style="left:409px">Quick Links</div>
<ul class="foot-list" style="left:409px;line-height:36px"><li>Home</li><li>About</li><li>Blog</li><li>Contact</li></ul>

<div class="foot-h" style="left:594px">About</div>
<p class="foot-about">Lorem ipsum dolor sit amet, consectetur adipiscing elit. Morbi fermentum laoreet ligula, vitae interdum purus accumsan a. Sed volutpat mauris</p>

<div class="foot-h" style="left:867px">Newsletter</div>
<div class="news-input">Enter email address</div>
<div class="news-btn">SUBSCRIBE</div>

<div class="abs copyright">© 2021 <em>Dance Studio</em>. All right reserved</div>

</body>
</html>
```